Mobile technology Business Card Design Project

We need a business card design for our company based in Sydeny Australia, that takes a company's desktop sites and creates a mobile site compatible to all mobile/smartphone devices. This allows greater ease of use and generally faster business conversion than customers using a desktop site.
Our company is called Zelvora but we refer to it as Zelvora Solutions. If this could be represented somewhere on the business card that would be great.
Am open to suggestions regarding the colours but a high tech  theme would be good.
Happy bidding!

Target Market(s)
Business owner that has a website and is reasonably savvy regarding online/mobile marketing.
Industry/Entity Type
Business
Requirements
Must have
- Business card details:
Director Peter Hawkley
Address: 4/15 Brenton rd, Kelmore. 2047
Email: tbc
Web: www.zelvora-example.com.au
The cards need to have two different names for the two directors.
Damien Ferrowe & Peter Hawkley (two separate business cards)

```html
<!DOCTYPE html>
<html lang="en">
<head>
<meta charset="utf-8">
<title>Zelvora Business Card</title>
<link rel="stylesheet" href="https://fonts.googleapis.com/css2?family=Questrial&display=swap">
<style>
  :root {
    --backdrop: #6a3826;
    --card-dark: #232323;
    --card-dark-edge: #151515;
    --card-light: #f3f3f3;
    --card-light-edge: #d2d2d2;
    --ink-light: #ffffff;
    --ink-dark: #1a1a1a;
    --accent-blue: #2d9ad6;
  }
  * { margin: 0; padding: 0; box-sizing: border-box; }
  html, body {
    width: 1200px; height: 1181px; overflow: hidden;
    background: var(--backdrop);
    font-family: "Questrial", "Century Gothic", sans-serif;
  }
  .canvas { position: relative; width: 1200px; height: 1181px; }
  .card {
    position: absolute; left: 260px; width: 680px;
    border-radius: 24px; overflow: hidden;
  }
  .card--front {
    top: 165px; height: 391px;
    background: radial-gradient(ellipse at 50% 35%, #3a3a3a 0%, var(--card-dark) 45%, var(--card-dark-edge) 100%);
    color: var(--ink-light);
  }
  .front-brand {
    position: absolute; left: 0; right: 0; top: 100px;
    display: flex; flex-direction: column; align-items: center;
  }
  .brand-dot {
    width: 134px; height: 134px; border-radius: 50%;
    background: var(--ink-light);
  }
  .front-name { margin-top: 10px; font-size: 30px; font-weight: normal; letter-spacing: 1px; line-height: 1; }
  .front-tagline { margin-top: 6px; font-size: 14px; letter-spacing: 0.8px; font-weight: bold; }

  .card--back { top: 617px; height: 390px; background: var(--card-dark); }
  .back-panel {
    position: absolute; left: 0; right: 0; top: 45px; height: 298px;
    background: radial-gradient(ellipse at 50% 45%, #fbfbfb 0%, var(--card-light) 40%, var(--card-light-edge) 100%);
  }
  .back-brand {
    position: absolute; left: 200px; top: 92px; width: 106px;
    display: flex; flex-direction: column; align-items: center;
  }
  .back-brand .brand-dot {
    width: 76px; height: 76px;
    background: var(--accent-blue);
  }
  .back-brand-name { margin-top: 8px; font-size: 18px; color: var(--ink-dark); }
  .divider {
    position: absolute; left: 339px; top: 93px; width: 2px; height: 111px;
    background: linear-gradient(to bottom, transparent, #222 20%, #222 80%, transparent);
  }
  .contact { position: absolute; left: 373px; top: 111px; color: var(--ink-dark); }
  .contact-name { font-size: 22px; line-height: 1.1; letter-spacing: 0.3px; }
  .contact-role { font-size: 13px; line-height: 1.1; }
  .contact-details { margin-top: 10px; font-size: 11px; line-height: 1.25; }
  .back-web {
    position: absolute; left: 0; right: 0; bottom: 15px;
    text-align: center; color: var(--ink-light); font-size: 12px; letter-spacing: 0.5px;
  }
</style>
</head>
<body>
<main class="canvas">
  <section class="card card--front" aria-label="Card front">
    <div class="front-brand">
      <span class="brand-dot" aria-hidden="true"></span>
      <h1 class="front-name">Zelvora</h1>
      <p class="front-tagline">Mobile Sites Made Simple</p>
    </div>
  </section>

  <section class="card card--back" aria-label="Card back">
    <div class="back-panel">
      <div class="back-brand">
        <span class="brand-dot" aria-hidden="true"></span>
        <span class="back-brand-name">Zelvora</span>
      </div>
      <div class="divider" aria-hidden="true"></div>
      <div class="contact">
        <p class="contact-name">Damien Ferrowe</p>
        <p class="contact-role">Director</p>
        <p class="contact-details">4/15 Brenton rd, Kelmore. 2047<br>yourname@zelvora-example.com</p>
      </div>
    </div>
    <p class="back-web">www.zelvora-example.com.au</p>
  </section>
</main>
</body>
</html>
```